Redesign of my Homepage - Online resource for anyone to learn American Sign Language

I would like to have a new homepage design http://www.SignPathora.com . My business is a website for anyone to learn American Sign Language. There are over 300 video lessons, with each lesson having 20 vocabulary words, retention exercises, 16,000 video dictionary etc. It is a very extensive site. It is a self paced website. If you need a log in to see what customers see, please let me know. I would like to keep the same color scheme. I want the website to look modern and clean. I want a fresh look! I want something that is easy to navigate, attracts customers, and easy to follow. I would like the final design to communicate that my website is for anyone to learn how to sign with this incredible program.

Target Market(s)

Students taking American Sign Language, Parents with Deaf children, future interpreters for the deaf, co-workers of the Deaf. Also, schools that offer American Sign Language (online schools, homeschools, etc. ).

Industry/Entity Type

Business

Number of Pages Required

1 page

Requirements
Must have
• My project must be very clean and clear. I want my homepage to show that this is a program for people to learn how American Sign Language.
Nice to have
• Not sure. Surprise me.

```html
<!DOCTYPE html>
<html lang="en">
<head>
<meta charset="utf-8">
<title>SignPathora – Learn American Sign Language</title>
<link href="https://fonts.googleapis.com/css2?family=Raleway:wght@400;500;600;700&family=Montserrat:wght@700;800&display=swap" rel="stylesheet">
<style>
:root{
  --green:#13c92c;
  --tan:#e0c08f;
  --dark:#1d1a19;
  --black:#000;
  --text:#333;
  --white:#fff;
  --grey:#f2f2f2;
}
*{margin:0;padding:0;box-sizing:border-box}
html,body{width:994px;height:1200px;overflow:hidden;background:var(--white)}
body{position:relative;font-family:'Raleway',sans-serif;color:var(--text)}
.abs{position:absolute}
.topbar{left:0;top:0;width:994px;height:25px;background:var(--grey)}
.login{top:6px;left:520px;display:flex;gap:5px;align-items:center;font-size:8px;color:#444}
.login .field{width:70px;height:11px;background:var(--tan);font-size:7px;padding-left:5px;line-height:11px;margin-right:6px}
.login .signin{width:54px;height:11px;background:var(--tan);font-size:6.5px;text-align:center;line-height:11px}
.social{display:flex;gap:2px}
.social span{width:9px;height:9px;background:#3b5998}
.social span:nth-child(2){background:#2aa3ef}
.social span:nth-child(3){background:#d63b2f}
.social span:nth-child(4){background:#0a66c2}
.social span:nth-child(5){background:#c8232c}
.top-social{top:7px;left:854px}
.brand{display:flex;align-items:center;gap:6px;font-weight:600;color:#3a2a1a}
.brand i{width:12px;height:12px;border-radius:50%;background:var(--green);display:block}
.logo{left:30px;top:30px;font-size:24px}
.logo small{display:block;font-size:7px;color:var(--green);font-weight:600;margin-top:-2px}
.nav{left:283px;top:48px;display:flex;height:36px;font-size:12.5px;color:#444}
.nav a{padding:0 11px;line-height:36px;text-decoration:none;color:inherit}
.nav a.active{background:var(--green);color:var(--white)}
.hero{left:0;top:84px;width:994px;height:318px;background:linear-gradient(90deg,#e8e4d8 0%,#f1ece2 40%,#ddd3c0 70%,#c8c0b0 100%)}
.hero h1{left:142px;top:94px;font-family:'Montserrat',sans-serif;font-weight:800;font-size:32px;color:#1a1a1a;letter-spacing:.5px}
.btn{background:var(--green);color:#1a1a1a;text-align:center}
.hero .btn{left:197px;top:153px;width:182px;height:38px;line-height:38px;font-size:16px}
.arrow{width:37px;height:37px;border-radius:50%;background:var(--white);display:flex;align-items:center;justify-content:center}
.tabs{top:368px;left:30px;display:flex;gap:4px}
.tabs div{height:34px;line-height:34px;text-align:center;font-size:17px;color:#333;background:var(--tan);width:218px}
.tabs div.on{background:var(--white)}
.card-img{top:417px;width:177px;height:180px;background:linear-gradient(160deg,#6f6a63,#3d3a37)}
.card-img h3{position:absolute;left:19px;top:65px;font-size:20px;font-weight:500;color:var(--white)}
.card-img p{position:absolute;left:19px;top:97px;font-size:9px;color:#eee}
.card-img hr{position:absolute;left:19px;top:116px;width:37px;border:0;border-top:2px solid #ddd}
.card-txt{top:604px;width:177px;height:72px;background:var(--tan);font-size:9.5px;padding:13px 19px;line-height:1.3}
.card-txt .btn{position:absolute;right:0;bottom:8px;width:70px;height:17px;line-height:17px;font-size:8.5px}
.news{left:599px;top:417px;width:319px;height:259px;background:linear-gradient(135deg,#7a726b,#4a4541 60%,#37332f)}
.news h3{position:absolute;left:27px;top:23px;font-size:17.5px;font-weight:500;color:var(--white)}
.news .circle{position:absolute;left:116px;top:65px;width:56px;height:56px;border:2px solid var(--white);border-radius:50%;display:flex;align-items:center;justify-content:center}
.news .email{position:absolute;left:27px;top:153px;width:235px;height:38px;background:var(--white);font-size:9px;padding-left:18px;line-height:38px;color:#555}
.news .btn{position:absolute;left:171px;top:206px;width:91px;height:30px;line-height:30px;font-size:12px}
.testi{left:0;top:694px;width:994px;height:134px;background:linear-gradient(90deg,#161413,#2b2724 50%,#3a332d 75%,#1a1817)}
.testi h2{position:absolute;left:30px;top:45px;font-size:21px;font-weight:500;color:var(--white)}
.testi .sub{position:absolute;left:32px;top:76px;font-size:9.5px;color:#ddd}
.quote-mark{position:absolute;left:188px;top:18px;font-family:'Montserrat',sans-serif;font-size:28px;color:var(--tan)}
.q{position:absolute;top:22px;width:136px;font-size:9px;line-height:1.33;color:#ddd}
.q b{display:block;font-weight:500;margin-top:10px}
.q.dim{color:#8a8580}
.vline{position:absolute;top:16px;width:1px;height:86px;background:#777}
.map{left:0;top:828px;width:994px;height:271px;background:linear-gradient(135deg,#e6e9e1,#dfe4d6 40%,#e8ebe6 70%,#d9e3cf)}
.map2{left:0;top:1174px;width:994px;height:26px;background:#e4e7df}
.flogo{left:33px;top:883px;font-size:19px}
.ftabs{top:870px;left:195px;display:flex;gap:4px}
.ftabs div{width:155px;height:32px;line-height:32px;background:var(--white);text-align:center;font-size:9px;font-weight:700;color:#222}
.follow{left:684px;top:872px;width:233px;height:205px;background:var(--white);padding:22px 27px;font-size:9px;color:#333}
.follow h4{font-size:9px;font-weight:700;margin-bottom:7px}
.info{display:flex;align-items:flex-start;gap:11px;margin-top:10px;line-height:1.6}
.info svg{flex:none;margin-top:2px}
.footer{left:0;top:1099px;width:994px;height:75px;background:var(--black);color:#ccc;font-size:7.5px;line-height:1.6;padding:18px 30px}
.footer .copy{margin-top:12px;color:#aaa}
.badge{left:849px;top:1112px;width:60px;height:48px;border-radius:50%;background:#d9b230}
</style>
</head>
<body>
<div class="abs topbar"></div>
<div class="abs login">User Name:<span class="field">••••••••</span>Passsword:<span class="field">••••••••</span><span class="signin">SIGN IN</span></div>
<div class="abs social top-social"><span></span><span></span><span></span><span></span><span></span></div>

<div class="abs logo"><div class="brand"><i></i>SignPathora</div><small>AMERICAN SIGN LANGUAGE</small></div>

<nav class="abs nav">
  <a class="active">Home</a><a>How it Works</a><a>Gift Certificates</a><a>Try It Free</a><a>Buy Now</a><a>Contact Us</a><a>Group Rate Form</a>
</nav>

<section class="abs hero" role="img" aria-label="Photo of a smiling young woman at a desk with a laptop and small potted plants beside a bright window">
  <h1 class="abs">Learn ASL ONLINE ?</h1>
  <div class="abs btn">Read More</div>
  <div class="abs arrow" style="left:35px;top:116px"><svg width="10" height="12" viewBox="0 0 10 12"><path d="M7 1 2 6l5 5" fill="none" stroke="#333" stroke-width="1.3"/></svg></div>
  <div class="abs arrow" style="left:879px;top:113px"><svg width="10" height="12" viewBox="0 0 10 12"><path d="M3 1l5 5-5 5" fill="none" stroke="#333" stroke-width="1.3"/></svg></div>
</section>

<div class="abs tabs"><div class="on">Learn ASL</div><div>Using ASL</div><div>Tutor Online</div><div>FREE Trial</div></div>

<div class="abs card-img" style="left:30px" role="img" aria-label="Group photo of a community gathering"><h3>Community</h3><p>Hearing Parents of Deaf Children</p><hr></div>
<div class="abs card-img" style="left:217px" role="img" aria-label="Photo of a parent with children"><h3>Parents</h3><p>Hearing Parents of Deaf Children</p><hr></div>
<div class="abs card-img" style="left:403px" role="img" aria-label="Photo of students with books"><h3>Students</h3><p>Hearing Parents of Deaf Children</p><hr></div>

<div class="abs card-txt" style="left:30px">Anyone that has a passion to learn American Sign Language (ASL)<div class="btn">Read More</div></div>
<div class="abs card-txt" style="left:217px">Learn to communicate more effectively with your child<div class="btn">Read More</div></div>
<div class="abs card-txt" style="left:403px">Learn to tackle the challenges you faced in the classroom<div class="btn">Read More</div></div>

<section class="abs news" role="img" aria-label="Photo of a woman with headphones using a laptop">
  <h3>Sign Up Recieve Newsletter</h3>
  <div class="circle"><svg width="22" height="30" viewBox="0 0 22 30"><path d="M11 2v25M2 18l9 9 9-9" fill="none" stroke="#fff" stroke-width="2"/></svg></div>
  <div class="email">@ type your email here</div>
  <div class="btn">SUBMIT</div>
</section>

<section class="abs testi" role="img" aria-label="Dark photo of two hands meeting in a handshake">
  <div class="quote-mark">“</div>
  <h2>Client Testimonials</h2>
  <div class="sub">We would like to hear your testimonial.</div>
  <svg class="abs" style="left:226px;top:58px" width="8" height="14" viewBox="0 0 8 14"><path d="M7 1 1 7l6 6" fill="none" stroke="#888"/></svg>
  <div class="q" style="left:253px">"I think the site is great...I've been showing my friends everything I learned all day...Your price is super reasonable and I can do everything on my own time, at my own pace."<b>Owen</b></div>
  <div class="vline" style="left:399px"></div>
  <div class="q dim" style="left:419px">"Hi! I just want to congratulate you...this is the website I have been waiting for...I love ASL and do not have any good classes in my community..."<b style="color:#ddd">Lucia</b></div>
  <div class="vline" style="left:569px"></div>
  <div class="q dim" style="left:585px">"I really like the dictionary part. I can select certain phrases and add them to my vocabulary."<b style="color:#ddd">Dana</b></div>
  <div class="vline" style="left:727px"></div>
  <div class="q" style="left:744px;width:150px">"This site is so cool! It teaches and covers all the basics so we recognize the sign, word, and finger spelling in a sentence. Excellent teaching tool. Thank you!! It is so easy to learn!!"<b>Hollis</b></div>
  <svg class="abs" style="left:910px;top:58px" width="8" height="14" viewBox="0 0 8 14"><path d="M1 1l6 6-6 6" fill="none" stroke="#888"/></svg>
</section>

<div class="abs map" role="img" aria-label="Street map of the surrounding area"></div>
<div class="abs flogo brand"><i></i>SignPathora</div>
<div class="abs ftabs"><div>Contact Us</div><div>Our Mission</div><div>Terms &amp; Conditions</div></div>

<div class="abs follow">
  <h4>Follow Us</h4>
  <div class="social"><span></span><span></span><span></span><span></span><span></span></div>
  <div class="info" style="margin-top:30px"><svg width="12" height="11" viewBox="0 0 12 11"><path d="M2 1h3l1 3-2 1c1 2 2 3 4 4l1-2 3 1v3C6 11 1 6 2 1z" fill="none" stroke="#333" stroke-width=".9"/></svg>(555) 204-7781</div>
  <div class="info" style="margin-top:2px"><svg width="12" height="9" viewBox="0 0 12 9"><rect x=".5" y=".5" width="11" height="8" fill="none" stroke="#333"/><path d="M.5.5 6 5l5.5-4.5" fill="none" stroke="#333"/></svg>questions@SignPathora.com.</div>
  <div class="info" style="margin-top:20px"><svg width="11" height="13" viewBox="0 0 11 13"><path d="M5.5 12S1 7.5 1 5a4.5 4.5 0 0 1 9 0c0 2.5-4.5 7-4.5 7z" fill="none" stroke="#333"/><circle cx="5.5" cy="5" r="1.6" fill="none" stroke="#333"/></svg><div>P.O. Box 55021<br>Maple Ridge, Ohio</div></div>
</div>

<footer class="abs footer">
  <p>SignPathora is a subscription based website for American Sign Language (ASL) video lessons. The content is for anyone who wishes to learn ASL, regardless of age. It has been designed to instruct deaf students,<br>parents of deaf children, and the community-at-large. You may cancel your subscription at any time. All lessons are taught by Deaf experts of ASL.</p>
  <p class="copy">SignPathora ©2017 All Rights Reserved</p>
</footer>
<div class="abs badge"></div>
<div class="abs map2" role="img" aria-label="Continuation of the street map"></div>
</body>
</html>
```